Designing business cards for my start-up business

The company is called Pellion. We are a start-up tech data company based in Guernsey, Channel Islands. We want the business cards to look clean, fresh and innovative, just what a tech company should be. We do not want the business cards to look corporate or too official such as a bank. I would like the front of the business card to have our logo and the tag line of "connecting talent". On the back will be our contact details, emails etc. However I am open to your ideas and suggestions. I have provided all our logos and a word doc of all our contact details. There are 4 directors of the business, so I want 4 versions of the same design.

Target Market(s)

Our clients are businesses of all industries. Its a broad target market.

Industry/Entity Type

Information Technology

Contact Information for Business Card

I have attached a word doc called "Business Cards info" which gives all contact details of the 4 employees for the company.

Requirements
Must have
• We must have our logo and the tag line of "connecting talent". This could on the front of the card and then the individuals contact details on the back. Other than that, I'm happy for the designers to come up with ideas/styles.
Nice to have
• N/A
Should not have
• I don't want the cards to look too formal or corporate. As mentioned, we are a tech start-up so we want to look innovative.

```html
<!DOCTYPE html>
<html lang="en">
<head>
<meta charset="utf-8">
<title>Pellion – Business Cards</title>
<link rel="stylesheet" href="https://fonts.googleapis.com/css2?family=Open+Sans:wdth,wght@75..100,400..800&display=swap">
<style>
  :root {
    --stage: #2a2a2c;
    --card: #0d0d0e;
    --card-sheen: #1c1c1e;
    --accent: #e8573a;
    --accent-deep: #d9482f;
    --grey-text: #8e8e90;
    --light-text: #d4d4d6;
    --white: #f2f2f2;
  }
  * { box-sizing: border-box; margin: 0; padding: 0; }
  html, body { width: 1200px; height: 900px; overflow: hidden; }
  body {
    background: var(--stage);
    font-family: "Open Sans", Arial, sans-serif;
    display: flex;
    flex-direction: column;
    align-items: center;
    justify-content: center;
    gap: 40px;
  }
  .card {
    position: relative;
    width: 700px;
    height: 400px;
    background: linear-gradient(135deg, var(--card-sheen) 0%, var(--card) 45%, var(--card) 100%);
    box-shadow: 0 10px 30px rgba(0,0,0,.45);
    overflow: hidden;
  }

  /* Brand lockup */
  .brand {
    position: absolute;
    display: flex;
    flex-direction: column;
    align-items: center;
    gap: 10px;
  }
  .brand-mark {
    width: 110px;
    height: 110px;
    background: var(--accent);
  }
  .brand-name {
    color: var(--white);
    font-weight: 700;
    font-size: 18px;
    letter-spacing: 8px;
    padding-left: 8px;
  }

  /* Front */
  .card-front .brand { left: 50%; top: 70px; transform: translateX(-50%); }
  .tagline {
    position: absolute;
    left: 50%;
    top: 250px;
    transform: translateX(-50%);
    color: var(--grey-text);
    font-weight: 700;
    font-stretch: 80%;
    font-variation-settings: "wdth" 80;
    font-size: 34px;
    letter-spacing: -0.5px;
    white-space: nowrap;
    line-height: 1;
  }
  .rule { position: absolute; height: 2px; background: var(--accent); }
  .card-front .rule-left { left: 0; width: 210px; top: 282px; }
  .card-front .rule-right { right: 0; width: 210px; top: 250px; }

  /* Back */
  .card-back .brand { left: 50px; top: 50px; }
  .holder {
    position: absolute;
    right: 50px;
    top: 70px;
    text-align: right;
  }
  .holder-name {
    color: var(--grey-text);
    font-weight: 700;
    font-stretch: 85%;
    font-variation-settings: "wdth" 85;
    font-size: 28px;
    line-height: 1.05;
    letter-spacing: -0.5px;
  }
  .holder-role {
    color: var(--accent);
    font-size: 17px;
    margin-top: 2px;
  }
  .card-back .rule-main { left: 0; width: 490px; top: 228px; }
  .contact-list {
    position: absolute;
    left: 120px;
    top: 246px;
    list-style: none;
    color: var(--light-text);
    font-size: 14px;
    line-height: 1.45;
  }
  .contact-list li { display: flex; align-items: flex-start; gap: 6px; }
  .contact-list svg { width: 13px; height: 13px; margin-top: 3px; flex: none; fill: var(--accent); }
  .contact-list .sep { color: var(--light-text); }
  .footer-band {
    position: absolute;
    left: 0; right: 0; bottom: 0;
    height: 14px;
    background: linear-gradient(90deg, var(--accent-deep), var(--accent));
  }
</style>
</head>
<body>

  <section class="card card-front" aria-label="Card front">
    <div class="brand">
      <div class="brand-mark"></div>
      <div class="brand-name">Pellion</div>
    </div>
    <div class="rule rule-left"></div>
    <div class="tagline">CONNECTING TALENT</div>
    <div class="rule rule-right"></div>
  </section>

  <section class="card card-back" aria-label="Card back">
    <div class="brand">
      <div class="brand-mark"></div>
      <div class="brand-name">Pellion</div>
    </div>
    <div class="holder">
      <div class="holder-name">LUC TOSTEVIN</div>
      <div class="holder-role">Director</div>
    </div>
    <div class="rule rule-main"></div>
    <ul class="contact-list">
      <li>
        <svg viewBox="0 0 16 16" aria-hidden="true"><path d="M8 1 1 7.5h2V15h4v-4h2v4h4V7.5h2z"/></svg>
        <span><span class="sep">: </span>12A Rue Marchande, Saint Aubin,<br>Guernsey, GY2 4QR, Channel Islands</span>
      </li>
      <li>
        <svg viewBox="0 0 16 16" aria-hidden="true"><path d="M3.5 1 6 4 4.6 5.8c.9 2 2.6 3.7 4.6 4.6L11 9l3 2.5-1.5 2.8C7 14 2 9 1.7 3.5z"/></svg>
        <span><span class="sep">: </span>+44 7700 900 318</span>
      </li>
      <li>
        <svg viewBox="0 0 16 16" aria-hidden="true"><path d="M1 3h14v10H1zm1.5 1.3v.4L8 8.6l5.5-3.9v-.4zm0 2.2v5.2h11V6.5L8 10.3z"/></svg>
        <span><span class="sep">: </span>Luc.Tostevin@pellion.gg</span>
      </li>
      <li>
        <svg viewBox="0 0 16 16" aria-hidden="true"><circle cx="8" cy="8" r="7"/></svg>
        <span><span class="sep">: </span>www.pellion.gg</span>
      </li>
    </ul>
    <div class="footer-band"></div>
  </section>

</body>
</html>
```